Commercial and Residential Paint Contractor needs website

We need a website for our residential painting, multi-family painting and commercial painting company. We paint interior and exterior of houses, apartments and commercial buildings. I would like an about us page, residential page, multi family page, commercial page and contact us. Need keywords added to website for seo opitimazation. I like this website https://www.velmorandhalestudio.com/

Target Market(s)

General Contractors and commercial property managers

Coding

Coded - Design and coding required

Number of Pages Required

5+ page

Font styles to use
Sans Serif

Requirements
Must have
• I need SEO keywords on pages

```html
<!DOCTYPE html>
<html lang="en">
<head>
<meta charset="utf-8">
<title>Halvern Painting — Residential, Multi Family &amp; Commercial Painting</title>
<link rel="stylesheet" href="https://fonts.googleapis.com/css2?family=Michroma&family=Poppins:wght@400;500;700&display=swap">
<style>
:root{
  --red:#b8102a;
  --navy:#15357a;
  --navy-dark:#14336f;
  --sky:#15a3ee;
  --roller:#1f93e8;
  --yellow:#fdc92c;
  --ink:#222;
  --white:#fff;
}
*{margin:0;padding:0;box-sizing:border-box}
html,body{width:1200px;height:2770px;overflow:hidden;background:var(--white)}
body{position:relative;font-family:"Poppins",sans-serif;color:var(--ink)}
.abs{position:absolute}
.heading{font-family:"Michroma",sans-serif;font-weight:400;white-space:nowrap}

/* header */
.logo{position:absolute;display:flex;align-items:center;gap:10px}
.logo-mark{width:16px;height:16px;background:var(--red)}
.logo-name{font-family:"Michroma",sans-serif;font-size:21px;line-height:1.15;color:var(--navy)}
.site-nav{position:absolute;top:54px;left:403px;font-family:"Michroma",sans-serif;font-size:12px;color:var(--navy)}
.site-nav a{color:inherit;text-decoration:none;position:absolute;white-space:nowrap}
.site-nav a.active{color:var(--red)}
.nav-tab{position:absolute;left:410px;top:0;width:28px;height:44px;background:var(--red);border-radius:0 0 4px 4px}

/* hero */
.hero-bg{position:absolute;left:0;top:0;width:1200px;height:760px;background:linear-gradient(90deg,#f6f6f7,#ececef)}
.hero-photo{position:absolute;left:640px;top:0;width:560px;height:760px;
  background:radial-gradient(ellipse at 60% 40%,var(--roller) 0 45%,#8fc9f3 62%,rgba(240,244,248,0) 75%)}
.hero-title{left:129px;top:266px;font-size:35px;line-height:44px;color:var(--red)}
.hero-text{left:130px;top:326px;width:500px;font-size:19.5px;line-height:26px;color:#333}
.brush-btn{position:absolute;width:204px;height:40px;border-radius:20px 8px 20px 8px;
  background:linear-gradient(90deg,#2d6fe8,#1c4fd6 60%,#4a8cf0);
  color:var(--white);font-family:"Michroma",sans-serif;font-size:14px;text-decoration:none;
  display:flex;align-items:center;justify-content:center;box-shadow:0 0 8px rgba(40,110,230,.5)}
.dots{left:133px;top:514px;display:flex;gap:18px}
.dots span{width:43px;height:4px;background:var(--red)}
.dots span:first-child{background:var(--navy)}
.wave{position:absolute;left:0;top:580px}

/* welcome */
.sec-title{font-size:28px;line-height:42px;color:var(--red)}
.welcome-title{left:121px;top:818px;font-size:21px;line-height:41px}
.body-text{font-size:15px;line-height:26px;color:#333}
.service-tile{position:absolute;display:flex;align-items:center;justify-content:center;
  font-family:"Michroma",sans-serif;font-size:15px;color:var(--white);border-radius:30px 60px 40px 70px}
.tile-res{left:441px;top:812px;width:311px;height:220px;background:linear-gradient(135deg,#3aa6d8,#2a89c2)}
.tile-com{left:769px;top:822px;width:317px;height:242px;background:linear-gradient(90deg,#3f9c45,#7fa9b0 55%,#b7bcc2)}

/* about */
.about-photo{left:0;top:1140px;width:677px;height:451px;border-radius:0 90px 120px 0;
  background:linear-gradient(135deg,#c9cdd2,#e8eaed 45%,#5566b8 70%,#dfe2e6)}
.checks{left:714px;top:1372px;list-style:none;font-size:14.5px;color:#333}
.checks li{display:flex;align-items:center;gap:16px;height:31px}

/* testimonial */
.band-blue{position:absolute;left:0;top:1700px}
.band-yellow{position:absolute;left:0;top:2010px}
.clients-title{left:0;width:1200px;top:1795px;text-align:center;font-size:28px;color:var(--white)}
.avatar{left:178px;top:1844px;width:130px;height:130px;border-radius:50%;border:6px solid var(--white);
  background:linear-gradient(160deg,#8a5a44,#c79a83)}
.quote{left:340px;top:1866px;width:520px;font-size:15.5px;line-height:26px;color:var(--white)}
.quote-name{left:336px;top:1950px;font-weight:700;font-size:20px;color:var(--white)}
.paint-can{left:849px;top:1817px;width:285px;height:263px;border-radius:50% 40% 45% 50%;
  background:radial-gradient(circle at 45% 45%,#1d58c8,#1548b0 55%,rgba(21,72,176,0) 72%)}

/* contact */
.contact-photo{left:0;top:2139px;width:484px;height:414px;border-radius:0 140px 0 0;
  background:linear-gradient(120deg,#f1ece6,#d9b49a 40%,#9a9ca0 75%,#f39a2f)}
.contact-title{left:564px;top:2116px;font-size:28px;color:#111}
.field{position:absolute;border:2px solid var(--white);font-size:15px;color:#333;padding:12px 20px}
.f-name{left:570px;top:2182px;width:451px;height:51px}
.f-email{left:574px;top:2254px;width:451px;height:51px}
.f-msg{left:574px;top:2322px;width:451px;height:105px}

/* footer */
.site-footer{position:absolute;left:0;top:2553px;width:1200px;height:217px;background:var(--navy-dark);color:var(--white)}
.site-footer .logo-name{color:var(--white);font-size:26px}
.foot-nav a{position:absolute;top:77px;font-family:"Michroma",sans-serif;font-size:12px;color:var(--white);text-decoration:none;white-space:nowrap}
.phone{position:absolute;left:98px;top:148px;font-weight:700;font-size:27px;letter-spacing:.5px}
.socials{position:absolute;left:974px;top:119px;display:flex;gap:20px}
.socials span{width:13px;height:13px;border-radius:50%;background:var(--white)}
.copy{position:absolute;left:896px;top:158px;font-size:10px}
.code{position:absolute;left:1134px;top:177px;font-size:12px;opacity:.8}
</style>
</head>
<body>

<div class="hero-bg"></div>
<div class="hero-photo" role="img" aria-label="Blue paint roller spreading blue paint on a white wall"></div>

<header>
  <div class="logo" style="left:114px;top:44px">
    <span class="logo-mark"></span>
    <span class="logo-name">HALVERN<br>PAINTING</span>
  </div>
  <div class="nav-tab"></div>
  <nav class="site-nav">
    <a class="active" style="left:0">HOME</a>
    <a style="left:74px">ABOUT US</a>
    <a style="left:184px">RESIDENTIAL</a>
    <a style="left:314px">MULTI FAMILY</a>
    <a style="left:447px">COMMERCIAL</a>
    <a style="left:586px">CONTACT US</a>
  </nav>
</header>

<h1 class="abs heading hero-title">HALVERN PAINTING</h1>
<p class="abs hero-text">Lorem ipsum dolor sit amet conse ctetur adipisicing elit, sed do eiusmod tempor incididunt ut labore et dolore magna.</p>
<a class="brush-btn" style="left:128px;top:425px">CONTACT US</a>
<div class="abs dots"><span></span><span></span><span></span></div>

<svg class="wave" width="1200" height="190" viewBox="0 0 1200 190" aria-hidden="true">
  <path d="M0 100 C120 30 300 -10 460 40 C640 100 820 150 1000 150 C1100 150 1170 120 1200 100 L1200 190 L0 190Z" fill="#fff"/>
  <path d="M0 100 C120 30 300 -10 460 40 C640 100 820 150 1000 150 C1100 150 1170 120 1200 100 L1200 112 C1170 135 1100 165 1000 163 C820 160 640 115 460 62 C300 20 130 50 10 150 Z" fill="var(--navy)"/>
  <path d="M10 150 C130 50 300 20 460 62 C600 100 700 128 780 140 C680 130 580 100 460 78 C300 50 140 80 6 188 Z" fill="var(--red)"/>
</svg>

<h2 class="abs heading sec-title welcome-title">WELCOME TO<br>HALVERN PAINTING</h2>
<p class="abs body-text" style="left:125px;top:914px;width:290px">Lorem ipsum dolor sit amet conse ctetur adipisicing elit, sed do eiusmod tempor incididunt ut labore et dolore magna.</p>
<a class="brush-btn" style="left:128px;top:1036px">READ MORE</a>
<div class="service-tile tile-res" role="img" aria-label="Blue painted bedroom interior">RESIDENTIAL</div>
<div class="service-tile tile-com" role="img" aria-label="Painters on ladders painting a commercial wall">COMMERCIAL</div>

<div class="abs about-photo" role="img" aria-label="Freshly painted living room with blue armchair and plants"></div>
<h2 class="abs heading sec-title" style="left:706px;top:1222px">ABOUT US</h2>
<p class="abs body-text" style="left:709px;top:1274px;width:380px">Lorem ipsum dolor sit amet conse ctetur adipisicing elit, sed do eiusmod tempor incididunt ut labore et dolore magna.</p>
<ul class="abs checks">
  <li><svg width="14" height="12" viewBox="0 0 14 12"><path d="M1 6l4 4 8-9" stroke="var(--red)" stroke-width="2.5" fill="none"/></svg>Same day service</li>
  <li><svg width="14" height="12" viewBox="0 0 14 12"><path d="M1 6l4 4 8-9" stroke="var(--red)" stroke-width="2.5" fill="none"/></svg>House painter service upon request</li>
  <li><svg width="14" height="12" viewBox="0 0 14 12"><path d="M1 6l4 4 8-9" stroke="var(--red)" stroke-width="2.5" fill="none"/></svg>Free colour consultation</li>
  <li><svg width="14" height="12" viewBox="0 0 14 12"><path d="M1 6l4 4 8-9" stroke="var(--red)" stroke-width="2.5" fill="none"/></svg>Residential and commercial services</li>
</ul>
<a class="brush-btn" style="left:712px;top:1535px">READ MORE</a>

<svg class="band-blue" width="1200" height="360" viewBox="0 0 1200 360" aria-hidden="true">
  <path d="M0 60 C200 40 420 20 700 15 C900 10 1080 25 1200 55 L1200 300 C1000 320 800 340 600 345 C400 350 200 330 0 320Z" fill="var(--sky)"/>
</svg>
<svg class="band-yellow" width="1200" height="545" viewBox="0 0 1200 545" aria-hidden="true">
  <path d="M420 40 C600 20 900 10 1200 0 L1200 545 L300 545 C340 400 380 200 420 40Z" fill="var(--yellow)"/>
</svg>

<h2 class="abs heading clients-title">WHAT OUR CLENTS SAYS</h2>
<div class="abs avatar" role="img" aria-label="Portrait of a client"></div>
<p class="abs quote">“Nulla tempor fermentum orci. Maecenas ac est hendrerit magna aliquam sagittis. Curabitur convallis interdum erat. Proin feugiat sem eu nisl. Aliquam erat volutpat.”</p>
<p class="abs quote-name">- Mira</p>
<div class="abs paint-can" role="img" aria-label="Open can of blue paint with a paintbrush"></div>

<div class="abs contact-photo" role="img" aria-label="Smiling woman holding a yellow paint roller"></div>
<h2 class="abs heading contact-title">CONTACT US</h2>
<div class="field f-name">Name</div>
<div class="field f-email">Email</div>
<div class="field f-msg">Message</div>
<a class="brush-btn" style="left:576px;top:2462px">SUBMIT</a>

<footer class="site-footer">
  <div class="logo" style="left:97px;top:60px">
    <span class="logo-name">HALVERN<br>PAINTING</span>
  </div>
  <div class="phone">1-800 555 0142</div>
  <nav class="foot-nav">
    <a style="left:402px">HOME</a>
    <a style="left:476px">ABOUT US</a>
    <a style="left:585px">RESIDENTIAL</a>
    <a style="left:715px">MULTI FAMILY</a>
    <a style="left:848px">COMMERCIAL</a>
    <a style="left:987px">CONTACT US</a>
  </nav>
  <div class="socials"><span></span><span></span><span></span><span></span></div>
  <div class="copy">© 2020 &nbsp;|&nbsp; www.halvernpainting.com</div>
  <div class="code">M1</div>
</footer>

</body>
</html>
```